Packaging design Project - for lovers of the distant lands of the Andes and it's organic culture

Oyé Oyé, friends of the organic terroir! Lovers of the distant lands and the Andes, this mission is for you!
Our baby, Verdant Ridge, is preparing for birth! This is your chance to make us dream.
Our values: Giving life to the Authentic Terroir of Bolivia. For it ; provide sustainable solutions for the local terroir of our organic crops.

What is the terroir? (french word). It’s that connection to Human and Earth. Humanity is respect for culture, ancestral know-how, artisanal work. The Earth is the environment, the ecology, this is what the Indians called the Pachamama.

At an altitude of 4200m, La Quinoa de Verdant Ridge is not cultivated in the plains with combine harvesters. It is cultivated by hand on the feet and on the mountainside. The fallow (66% of the land) allows the soil and the Gods of the Andean cosmovision to come to life.
Our mission is to bring these values to life through these products that we import; White Quinoa , red, Duo (red and white) and Trio (red, black and white).
For this, we are looking for a packaging design. You bring creativity and together we validate the content !

The finished product is intended for end consumers (specialized organic store for example). Its format is 18cm high x 8.5cm long and 4.5cm wide. We therefore need a graphic charter for the entire packaging; or 4 sides totaling 26 cm for 18 cm high. You will mainly work on the visual of the main page (18x8.5), illustration of our committed values through the colors of Bolivia: Red, Yellow and Green. The country being very colorful by nature (google search: "Aguayo cloth") we want to create a breath of life through the liveliness of the colors, that the products are obvious, just like these famous Bolivian Aguayo.
Our Quinoa comes from an authentic terroir. It is harvested by hand and is very rich in nutrition.
We had already worked on packaging, which we want to improve and make more alive. It’s true that the black print kraft background isn’t the best.
Here are some snippets of text taken from this first packaging:
"While the Quinoa of the plains depletes the soils of the Bolivian altiplano ..."
"The Verdant Ridge Quinoa comes from areas that are difficult to access, at the foot and on the mountainside where the cultivation is done by hand and with respect for ancestral traditions"
Mountain Quinoa committed!
Provides a local solution for the Bolivian terroir.
By respecting the Earth: the Pachamama with the fallow of 66% of the land. A return to the sources, as in the time of the Incas, letting the llamas make the biodiversity of the high plains flourish.
By respect for the Human Being and for future generations. Cultivated and distributed preserving the essence of Andean culture, the rights and croyances of Quechua producers and honoring the values of the Bolivian people.

In summary, I invite you to discover the energy of the project through this video: https://www.clipvaultex.com/watch?v=4TkPzLa-q9R
And these few images (attachments)…
And our logo of course on the PDF of our project presentation!

Note: Ideally, the design could include a visual of the raw Quinoa so client could see the product on the packaging. (as enclosed pictures!!!)

And most of all... have fun! Let your creativity EXPLODE! That's exactly what we want you to do. Just plenty be yourself... that's how our client will say 'Whaow!' looking at your art!

enjoy!

Target Market(s)

Premium Quinoa consumers. - Engaged consumers for causes and belief throught their product consumption

Font styles to use
Other font styles liked:
• earth quest (for head lines)

Colors
acd136
9bcb3c
ec1f27
f04a50
f78f20
f37122
ffc214
fece3e
fbed22

Requirements
Must have
• Colors (red, green and yellow)
Mountain as backgroud (enclosed)
Quinoa field on the feet or aside the mountain
Autoctones (people)
Quinoa grains (as it is raw)
Nice to have
• Detail of expressing Quinoa is handly cultivated (hand harvest)
Tipical houses in the back
Aguayo motifs (for the graphic charter maybe?)

```html
<!DOCTYPE html>
<html lang="fr">
<head>
<meta charset="utf-8">
<title>Verdant Ridge – Quinoa Real Blanc</title>
<link rel="stylesheet" href="https://fonts.googleapis.com/css2?family=Kaushan+Script&family=Lobster&family=Caveat+Brush&display=swap">
<style>
  :root {
    --page: #ffffff;
    --pack-black: #1a1a1a;
    --stripe: #2b2b2b;
    --andes-green: #1f8a3c;
    --andes-yellow: #f7a21b;
    --sun-yellow: #ffc214;
    --andes-red: #ec1f27;
    --andes-orange: #f37122;
    --white: #ffffff;
  }
  * { margin: 0; padding: 0; box-sizing: border-box; }
  html, body {
    width: 1200px; height: 2400px; overflow: hidden;
    background: var(--page);
  }
  .pack-front {
    position: absolute;
    left: 128px; top: 200px;
    width: 942px; height: 2000px;
    overflow: hidden;
    background:
      repeating-linear-gradient(to bottom, var(--pack-black) 0 7px, var(--stripe) 7px 9px);
    box-shadow: 0 18px 40px rgba(0,0,0,.45);
  }
  .brand-mark {
    position: absolute; left: 291px; top: 140px;
    width: 380px; height: 380px;
    border-radius: 50%;
    background: linear-gradient(to bottom, var(--andes-red) 0%, var(--andes-orange) 30%, var(--sun-yellow) 58%, var(--andes-green) 100%);
  }
  .brand {
    position: absolute; left: 0; right: 0; top: 540px;
    text-align: center;
    font-family: "Caveat Brush", cursive;
    font-weight: 400;
    font-size: 118px; line-height: 1;
    color: var(--andes-green);
  }
  .brand-tagline {
    position: absolute; left: 0; right: 0; top: 660px;
    text-align: center;
    font-family: "Caveat Brush", cursive;
    font-size: 78px; line-height: 1;
    color: var(--sun-yellow);
  }
  .product-name {
    position: absolute; left: 172px; top: 812px;
    font-family: "Lobster", cursive;
    font-weight: 400;
    font-size: 218px; line-height: 1.1;
    color: var(--andes-yellow);
    -webkit-text-stroke: 9px var(--white);
    paint-order: stroke fill;
  }
  .product-origin {
    position: absolute; right: 168px; top: 1062px;
    font-family: "Kaushan Script", cursive;
    font-size: 40px; line-height: 1;
    color: var(--white);
  }
  .benefit-pill {
    position: absolute; left: 165px; top: 1167px;
    width: 623px; height: 72px;
    border-radius: 36px;
    background: var(--andes-yellow);
    display: flex; align-items: center; justify-content: center;
    font-family: "Kaushan Script", cursive;
    font-size: 46px;
    color: var(--white);
  }
  .variety {
    position: absolute; left: 0; width: 916px; top: 1300px;
    text-align: center;
    font-family: "Kaushan Script", cursive;
    font-size: 68px; line-height: 1;
    color: var(--white);
  }
  .andes-scene {
    position: absolute; left: 0; right: 0; bottom: 0;
    height: 582px;
  }
</style>
</head>
<body>
  <main class="pack-front">
    <div class="brand-mark" aria-hidden="true"></div>
    <h1 class="brand">Verdant Ridge</h1>
    <p class="brand-tagline">Terroir Authentique</p>

    <h2 class="product-name">Quinoa</h2>
    <p class="product-origin">de montagnes de Bolivie</p>

    <p class="benefit-pill">a haute valeur nutritive</p>

    <p class="variety">Real Blanc</p>

    <svg class="andes-scene" viewBox="0 0 942 582" preserveAspectRatio="none" role="img" aria-label="Illustration area: Andean mountains under a starry sky with a Quechua grower and quinoa fields, in Bolivian green, yellow and red">
      <defs>
        <linearGradient id="bolivia-sweep" x1="0" y1="0" x2="1" y2="0">
          <stop offset="0" stop-color="#0f8a45"/>
          <stop offset="0.5" stop-color="#f7b51b"/>
          <stop offset="0.8" stop-color="#f37122"/>
          <stop offset="1" stop-color="#e42527"/>
        </linearGradient>
      </defs>
      <rect x="0" y="0" width="942" height="582" fill="url(#bolivia-sweep)"/>
    </svg>
  </main>
</body>
</html>
```